KV MOTORS BANNER/SIGN DESIGN

Design a banner sign for outdoor use for KV MOTORS - a premium pre owned vehicle sales center. The size must be 36 feet in width
and 3 feet in height.

Information required: logo (attached)
-PREMIUM PRE-OWEND VEHICLE SALES
- 403.555.0172

perhaps in smaller font: BUY-SELL-TRADE

prefer white background but could possibly do red matching the logo

```html
<!DOCTYPE html>
<html lang="en">
<head>
<meta charset="utf-8">
<title>KV Motors Banner</title>
<link href="https://fonts.googleapis.com/css2?family=Audiowide&family=Montserrat:wght@800&display=swap" rel="stylesheet">
<style>
  :root {
    --page-bg: #eef2f4;
    --brand-red: #da1f26;
    --white: #ffffff;
    --ink: #222222;
    --pill-edge: #f3a3a6;
    --photo-sky: #9fb6cc;
    --photo-trees: #3d5a2c;
    --photo-road: #5d5f60;
  }
  * { margin: 0; padding: 0; box-sizing: border-box; }
  html, body {
    width: 1200px;
    height: 600px;
    overflow: hidden;
    background: var(--page-bg);
  }
  .banner {
    position: absolute;
    left: 20px;
    top: 244px;
    width: 1160px;
    height: 111px;
    overflow: hidden;
    background: var(--brand-red);
  }
  .banner__photo {
    position: absolute;
    left: 0;
    top: 0;
    width: 270px;
    height: 111px;
    background: linear-gradient(180deg, var(--photo-sky) 0%, var(--photo-trees) 35%, var(--photo-trees) 70%, var(--photo-road) 100%);
  }
  .banner__art {
    position: absolute;
    inset: 0;
    width: 1160px;
    height: 111px;
  }
  .headline {
    font-family: "Audiowide", sans-serif;
    font-size: 34px;
    fill: var(--white);
  }
  .tagline {
    font-family: "Montserrat", sans-serif;
    font-weight: 800;
    font-size: 17px;
    fill: var(--white);
  }
  .brand-name {
    font-family: "Montserrat", sans-serif;
    font-weight: 800;
    font-size: 13px;
    fill: var(--ink);
  }
  .phone {
    font-family: "Audiowide", sans-serif;
    font-size: 23px;
    fill: var(--brand-red);
  }
</style>
</head>
<body>
  <div class="banner">
    <div class="banner__photo" role="img" aria-label="Photo of a white convertible sports car parked in front of trees"></div>
    <svg class="banner__art" viewBox="0 0 1160 111" xmlns="http://www.w3.org/2000/svg">
      <path class="banner__wave" d="M232 0 Q266 28 250 55 Q234 84 242 111 L1160 111 L1160 0 Z" fill="var(--white)"/>
      <path class="banner__field" d="M246 0 Q280 28 264 55 Q248 84 258 111 L1160 111 L1160 0 Z" fill="var(--brand-red)"/>

      <text class="headline" x="288" y="48" textLength="815" lengthAdjust="spacingAndGlyphs" transform="skewX(-10)" transform-origin="695 40">PREMIUM PRE - OWNED VEHICLE SALES</text>

      <text class="tagline" x="270" y="83" textLength="179" lengthAdjust="spacing">BUY-SELL-TRADE</text>
      <text class="tagline" x="934" y="83" textLength="180" lengthAdjust="spacing">BUY-SELL-TRADE</text>

      <rect class="contact-pill" x="471" y="53" width="444" height="41" rx="20.5" fill="var(--white)" stroke="var(--pill-edge)" stroke-width="2"/>
      <circle class="brand-dot" cx="498" cy="74" r="11" fill="var(--brand-red)"/>
      <text class="brand-name" x="516" y="79" textLength="85" lengthAdjust="spacing">KV MOTORS</text>
      <text class="phone" x="625" y="83" textLength="276" lengthAdjust="spacing">403.555.0172</text>
    </svg>
  </div>
</body>
</html>
```